House-share and Room Rental Website (With Focus on the Bedroom Landing Page)

Looking for website design for our House-share (executive accommodation) and room rental business.

Our company name is: Lodvenra could also be written as LodVenra or lodvenra. Either is fine .. just looking for a nice clean catchy logo to go with the design.

EXAMPLES
These are examples of other websites in this field that are doing well. this is a kind of baseline.
https://kelbrin.com.au/
https://www.tuvaplex.com/
https://www.nestorvi.com/
https://www.quillsa.net/
https://www.pendlebarrow.com.au/

Our business model is to rent rooms to people looking for high-quality accommodation. We fill the gap between those looking to rent rooms and those with rooms to rent. However, our model is slightly different from those already on the market as we looking to fill a massive gap in the market delivering upmarket rooms for rent.(Executive Accommodation) also in the back end will be coupled with a self management process in the back end.

We offer executive style accommodation that stands out above the rest. With special extras like fire safety.. and management processes that create happier homes. We are looking for a web design package that can help us grow and scale our business. We need a design that is captivating

Our MAIN focus is having a room landing page that stands out from the rest... The core of our business will rely on the promotion of the rooms in a share house... so the whole design relies on the BEDROOM landing page to drive results.

Target Market(s)

We have 2 markets we are aiming at ... the first market is people offering rooms to rent who want the highest rental return. The second market is people looking to rent safe, high-quality rooms, in houses that are well managed and looked after.

Industry/Entity Type

Share Economy

Logo Text

LodVenra

Number of Pages Required

5+ page

Font styles to use
Sans Serif

Colors
3276b5

Requirements
Must have
• A messaging system whereby we can create direct communication between those offering rooms and those looking for rooms.
• A call to action that says " Schedule an Inspection"
• Landing page for promoting rooms
• A home page for showing stock.
• Profile page for those selling rooms
• Profile page for those looking for rooms.
• A scheduling calendar for booking inspections
Nice to have
• Pages where new residents can lock in a room.. pay bond and rents.. and sign contracts
• Notifications
• SMS capabilities in the backend.
Should not have
• No script or handwriting fonts.

```html
<!DOCTYPE html>
<html lang="en">
<head>
<meta charset="utf-8">
<title>LodVenra — Executive Rooms</title>
<link href="https://fonts.googleapis.com/css2?family=Fira+Sans:wght@400;500;600;700&family=Open+Sans:wght@400;600;700&display=swap" rel="stylesheet">
<style>
:root{
  --navy:#34465f;
  --navy-dark:#2b3a50;
  --blue:#3276b5;
  --blue-dark:#285f93;
  --gold:#d8b11d;
  --gold-soft:#c9a84a;
  --grey-bg:#efefef;
  --line:#d8d8d8;
  --text:#4a4a4a;
  --muted:#8a8a8a;
  --white:#ffffff;
  --green:#3aa53a;
  --teal:#3bb59b;
  --plum:#9a55a8;
  --ink:#1f2633;
}
*{box-sizing:border-box;margin:0;padding:0}
html,body{width:712px;height:1200px;overflow:hidden}
body{position:relative;background:var(--white);font-family:"Open Sans",Arial,sans-serif;color:var(--text)}
.abs{position:absolute}

/* top bar */
.topbar{left:0;top:0;width:712px;height:11px;background:var(--gold)}
.topbar span{position:absolute;top:2px;font-size:5px;color:var(--white);font-weight:600}
.flag{position:absolute;top:3px;width:7px;height:5px;background:var(--white);border:1px solid var(--blue)}
.lang-on{position:absolute;left:538px;top:0;width:26px;height:11px;background:var(--navy)}

/* header */
.logo-mark{left:59px;top:15px;width:17px;height:17px;background:var(--blue)}
.logo-name{left:80px;top:12px;font-family:"Fira Sans",Arial,sans-serif;font-size:18px;font-weight:500;color:var(--navy);letter-spacing:.2px}
.tagline{left:59px;top:41px;font-size:5px;color:var(--muted)}
.city{left:128px;top:38px;width:56px;height:11px;background:var(--navy);color:var(--gold);font-size:5px;text-align:center;line-height:11px;font-weight:600}
.weather{left:215px;top:20px;font-size:5px;color:var(--muted);line-height:6.5px}
.weather b{color:var(--gold);font-size:7px}
.phone{left:296px;top:23px;font-family:"Fira Sans",Arial,sans-serif;font-size:11px;font-weight:600;color:var(--navy)}
.phone-sub{left:296px;top:36px;font-size:4.5px;color:var(--muted)}
.address{left:446px;top:24px;font-size:6.5px;color:var(--ink)}
.address-sub{left:460px;top:35px;font-size:4.5px;color:var(--muted);text-decoration:underline}
.onmap{left:421px;top:35px;font-size:4.5px;color:var(--gold);text-decoration:underline}
.btn-cta{left:540px;top:26px;width:113px;height:16px;background:var(--blue);border-radius:8px;color:var(--white);font-size:5px;font-weight:700;text-align:center;line-height:16px;letter-spacing:.2px}

/* nav */
.nav{left:0;top:54px;width:712px;height:17px;background:var(--navy);border-bottom:2px solid var(--blue)}
.nav span{position:absolute;top:5px;font-size:5px;color:var(--gold);font-weight:600;letter-spacing:.1px}

/* hero */
.hero{left:0;top:71px;width:712px;height:166px;background:linear-gradient(100deg,#e8dccb 0%,#c9a57c 35%,#b48e64 60%,#d9c4a3 100%)}
.hero-card{left:450px;top:110px;width:197px;height:98px;background:rgba(60,60,60,.62)}
.hero-card h2{position:absolute;left:9px;top:9px;font-family:"Fira Sans",Arial,sans-serif;font-size:9px;color:var(--gold);font-weight:600}
.hero-card .tour{position:absolute;left:20px;top:33px;font-size:4.5px;color:var(--gold);font-weight:600}
.hero-card .tour-ico{position:absolute;left:9px;top:32px;width:8px;height:6px;border:1px solid var(--gold)}
.hero-card p{position:absolute;left:9px;top:43px;width:180px;font-size:4.2px;color:#e8e8e8;line-height:5.5px}
.hero-card .price{position:absolute;left:9px;top:76px;font-family:"Fira Sans",Arial,sans-serif;font-size:10px;color:var(--gold)}
.hero-card .btn{position:absolute;left:100px;top:75px;width:93px;height:15px;background:var(--blue);border-radius:7px;color:var(--white);font-size:4.5px;text-align:center;line-height:15px;font-weight:700}
.hero-dot{position:absolute;top:223px;width:31px;height:3px;background:var(--white)}

/* quick links */
.quick span{position:absolute;top:257px;font-size:5px;color:var(--navy);text-decoration:underline}
.quick .ico{position:absolute;top:250px;width:18px;height:18px;border-radius:50%;background:#f1f1f1;border:1px solid #e2e2e2}

/* search band */
.search{left:0;top:277px;width:712px;height:69px;background:var(--navy);border-top:2px solid var(--navy-dark)}
.search .big{position:absolute;font-family:"Fira Sans",Arial,sans-serif;font-size:11px;color:var(--gold);font-weight:600}
.search .label{position:absolute;font-size:5.5px;color:var(--gold);font-weight:600}
.datebox{position:absolute;top:13px;width:89px;height:20px;border:1px solid var(--gold);color:var(--gold);font-family:"Fira Sans",Arial,sans-serif;font-size:10px;line-height:18px;padding-left:24px}
.datebox svg{position:absolute;left:6px;top:4px}
.person{position:absolute;top:28px;width:8px;height:8px;border-radius:50%;border:1px solid var(--gold)}
.person.on{background:var(--gold)}
.select{position:absolute;left:114px;top:43px;width:95px;height:16px;background:var(--navy-dark);color:var(--gold);font-size:5.5px;line-height:16px;padding-left:6px}
.pricebox{position:absolute;top:43px;height:18px;border:1px solid var(--gold);color:var(--gold);font-size:5.5px;text-align:center;line-height:16px}
.btn-choose{position:absolute;left:530px;top:43px;width:97px;height:17px;background:var(--gold);border-radius:8px;color:var(--white);font-size:6px;font-weight:700;text-align:center;line-height:17px}

/* rooms */
.rooms{left:0;top:346px;width:712px;height:272px;background:var(--grey-bg);border-bottom:1px solid #cfcfcf}
.card{position:absolute;top:14px;width:144px;background:var(--white)}
.card .photo{height:80px}
.card .kind{margin-top:6px;text-align:center;font-size:4.5px;color:var(--gold-soft)}
.card .rate{text-align:center;font-family:"Fira Sans",Arial,sans-serif;font-size:10px;font-weight:600;color:var(--ink);margin-top:2px}
.card .amen{display:flex;flex-wrap:wrap;padding:5px 4px 0 4px}
.card .amen span{width:45px;font-size:3.6px;color:var(--ink);font-weight:600;display:flex;align-items:center;gap:2px;height:9px}
.card .amen i{display:inline-block;width:6px;height:6px;border:1px solid var(--gold);border-radius:1px}
.card .foot{display:flex;justify-content:space-between;border-top:1px solid var(--line);margin:4px 4px 0 4px;padding-top:3px;font-size:3.6px}
.card .foot b{color:var(--ink)}
.card .foot em{font-style:normal;color:var(--gold-soft)}
.card .btn{display:block;margin:8px auto 8px;width:90px;height:15px;background:var(--blue);border-radius:8px;color:var(--white);font-size:4.3px;text-align:center;line-height:15px;font-weight:700}
.roundbtn{position:absolute;width:25px;height:25px;border-radius:50%;background:var(--blue)}
.more-label{font-size:5.5px;font-weight:700;color:var(--ink);letter-spacing:.4px}
.more-link{font-size:5.5px;font-weight:700;color:var(--blue);text-decoration:underline;letter-spacing:.4px}

/* deals */
.sec-title{font-family:"Fira Sans",Arial,sans-serif;font-size:13px;font-weight:600;color:var(--navy);letter-spacing:.3px}
.hot{left:141px;top:663px;font-size:7.5px;color:#e32222;font-weight:700}
.deal-slide{left:59px;top:694px;width:295px;height:170px;background:linear-gradient(90deg,#7c8d4c 0%,#c8c2b4 40%,#e9dfdc 65%,#c6b3b2 100%)}
.deal-box{left:109px;top:730px;width:199px;height:96px;background:rgba(255,255,255,.82);border:1px solid var(--white)}
.deal-box .a{position:absolute;top:13px;width:100%;text-align:center;font-size:5.5px;color:var(--navy)}
.deal-box .b{position:absolute;top:21px;width:100%;text-align:center;font-family:"Fira Sans",Arial,sans-serif;font-size:16px;color:var(--navy);font-weight:500}
.deal-box .c{position:absolute;top:44px;width:100%;text-align:center;font-size:5.5px;color:var(--navy)}
.deal-box .d{position:absolute;left:22px;top:59px;width:154px;height:17px;background:var(--white);border-radius:9px;text-align:center;line-height:17px;font-family:"Fira Sans",Arial,sans-serif;font-size:8.5px;font-weight:600;color:var(--gold)}
.slide-arrow{position:absolute;top:770px;width:20px;height:20px;background:rgba(255,255,255,.75)}
.tile{position:absolute;top:874px;height:78px;display:flex;flex-direction:column;align-items:center;justify-content:center;text-align:center;color:var(--white);font-family:"Fira Sans",Arial,sans-serif;font-weight:600;line-height:8px}
.tile .inner{position:absolute;left:4px;top:4px;right:4px;bottom:4px;border:1px solid rgba(255,255,255,.9)}
.pager{position:absolute;top:964px;width:17px;height:3px;background:#e0e0e0}

/* reviews */
.promo{left:410px;top:693px;width:194px;height:34px;background:#f8e10a}
.promo .cut{position:absolute;left:48px;top:2px;height:30px;border-left:1px dashed var(--ink)}
.promo span{position:absolute;left:59px;top:10px;font-size:5.5px;font-weight:700;color:var(--ink);line-height:7.5px;text-decoration:underline}
.review{position:absolute;left:410px;width:244px}
.avatar{position:absolute;left:0;top:0;width:57px;height:57px;border-radius:50%;border:4px solid var(--green)}
.avatar div{width:100%;height:100%;border-radius:50%;border:2px solid var(--white)}
.who{position:absolute;left:0;top:62px;width:57px;text-align:center}
.who b{display:block;font-size:4.5px;color:var(--ink);letter-spacing:.3px}
.who small{display:block;font-size:3px;color:var(--muted);line-height:4px;margin-top:2px}
.rating{position:absolute;left:70px;top:0;display:flex;align-items:center;gap:6px}
.rating .lbl{font-size:4.5px;font-weight:700;color:var(--ink)}
.rating .score{font-family:"Fira Sans",Arial,sans-serif;font-size:11px;font-weight:600;color:var(--navy)}
.review p{position:absolute;left:70px;top:16px;width:174px;font-size:5px;line-height:8px;color:var(--text)}
.review a{font-size:4px;font-weight:700;color:var(--blue);text-decoration:underline}

/* footer */
.footer{left:0;top:1142px;width:712px;height:58px;background:var(--navy)}
.footer .col{position:absolute;font-size:4.5px;line-height:10px}
.footer .col span{display:block}
.footer .light{color:var(--gold-soft)}
.footer .strong{color:var(--gold);font-weight:600}
.feedback{position:absolute;left:257px;top:16px;width:72px;height:13px;background:var(--blue-dark);border-radius:7px;color:var(--white);font-size:4.5px;line-height:13px;padding-left:24px}
.footer .info{position:absolute;top:18px;font-size:4.5px;color:var(--gold);text-decoration:underline}
.copy{left:0;top:1184px;width:712px;height:16px;background:var(--navy-dark);border-top:1px solid #4a5d78}
.copy span{position:absolute;left:59px;top:5px;font-size:4.5px;color:var(--gold-soft)}
</style>
</head>
<body>

<!-- top bar -->
<div class="abs topbar">
  <span style="left:60px">●</span>
  <span style="left:69px">Live Room Tours</span>
  <span style="left:273px">◎</span>
  <span style="left:286px;text-decoration:underline">House virtual tour</span>
  <div class="lang-on"></div>
  <div class="flag" style="left:541px"></div><span style="left:551px">EN</span>
  <div class="flag" style="left:570px"></div><span style="left:580px">RU</span>
  <span style="left:609px">◉ Rent in:</span><div class="flag" style="left:638px"></div><span style="left:648px">$</span>
</div>

<!-- header -->
<div class="abs logo-mark"></div>
<div class="abs logo-name">LodVenra</div>
<div class="abs tagline">Make yourself at home in:</div>
<div class="abs city">YOUR CITY</div>

<svg class="abs" style="left:196px;top:20px" width="16" height="14" viewBox="0 0 16 14" aria-hidden="true">
  <circle cx="6" cy="5" r="3" fill="none" stroke="#d8b11d" stroke-width="1"/>
  <path d="M3 12h9a3 3 0 0 0 0-6 4 4 0 0 0-7 1 2.5 2.5 0 0 0-2 5z" fill="#fff" stroke="#d8b11d" stroke-width="1"/>
</svg>
<div class="abs weather">Partly cloudy<br><b>26°</b><br>possibility of thunder</div>

<div class="abs phone">+7 800 555 0142</div>
<div class="abs phone-sub">hot line</div>
<svg class="abs" style="left:384px;top:24px" width="10" height="10" viewBox="0 0 10 10" aria-hidden="true"><circle cx="5" cy="5" r="4" fill="none" stroke="#d8b11d" stroke-width="1.4"/><circle cx="5" cy="5" r="1.5" fill="#d8b11d"/></svg>

<svg class="abs" style="left:424px;top:19px" width="12" height="15" viewBox="0 0 12 15" aria-hidden="true"><path d="M6 1a4 4 0 0 0-4 4c0 3 4 8 4 8s4-5 4-8a4 4 0 0 0-4-4z" fill="none" stroke="#d8b11d" stroke-width="1.2"/><circle cx="6" cy="5" r="1.4" fill="#d8b11d"/></svg>
<div class="abs onmap">On map</div>
<div class="abs address">Larkmoor street, 1A</div>
<div class="abs address-sub">More houses</div>
<div class="abs btn-cta">SCHEDULE AN INSPECTION</div>

<!-- nav -->
<nav class="abs nav">
  <span style="left:59px">ROOMS</span>
  <span style="left:126px">OUR HOUSES</span>
  <span style="left:206px">TERMS OF TENANCY</span>
  <span style="left:364px">MESSAGES</span>
  <span style="left:444px">REVIEWS</span>
  <span style="left:511px">CONTACTS</span>
  <span style="left:585px">LIST YOUR ROOM</span>
</nav>

<!-- hero -->
<div class="abs hero" role="img" aria-label="Photo of a bright shared living room with a grey corner sofa, cushions and a vase of flowers"></div>
<svg class="abs" style="left:14px;top:138px" width="16" height="24" viewBox="0 0 16 24" aria-hidden="true"><path d="M13 2 3 12l10 10" fill="none" stroke="#222" stroke-width="1.4"/></svg>
<svg class="abs" style="left:682px;top:138px" width="16" height="24" viewBox="0 0 16 24" aria-hidden="true"><path d="m3 2 10 10L3 22" fill="none" stroke="#222" stroke-width="1.4"/></svg>
<div class="abs hero-card">
  <h2>SINGLE ROOM TOP FLOOR</h2>
  <div class="tour-ico"></div>
  <div class="tour">ROOM VIRTUAL TOUR</div>
  <p>Executive rooms in well managed share houses with views of the Velmara river or a quiet green garden. Fully furnished, with fire safety, fast Wi-Fi and weekly cleaning ...</p>
  <div class="price">$280 / WEEK</div>
  <div class="btn">SCHEDULE AN INSPECTION</div>
</div>
<div class="hero-dot" style="left:283px"></div>
<div class="hero-dot" style="left:324px;background:var(--gold)"></div>
<div class="hero-dot" style="left:364px"></div>
<div class="hero-dot" style="left:405px"></div>

<!-- quick links -->
<div class="quick">
  <div class="ico" style="left:122px"></div>
  <svg class="abs" style="left:127px;top:254px" width="8" height="10" viewBox="0 0 8 10" aria-hidden="true"><path d="M4 1a3 3 0 0 0-3 3c0 2 3 5 3 5s3-3 3-5a3 3 0 0 0-3-3z" fill="none" stroke="#34465f"/></svg>
  <span style="left:149px">HOW TO GET THERE?</span>
  <div class="ico" style="left:301px"></div>
  <svg class="abs" style="left:305px;top:256px" width="10" height="7" viewBox="0 0 10 7" aria-hidden="true"><rect x="1" y=".5" width="8" height="5" rx="1" fill="none" stroke="#34465f"/><path d="M3 5.5 2 7" stroke="#34465f"/></svg>
  <span style="left:329px">message the host</span>
  <div class="ico" style="left:476px"></div>
  <svg class="abs" style="left:481px;top:254px" width="8" height="10" viewBox="0 0 8 10" aria-hidden="true"><path d="M1 1v8M1 1h6l-1 2 1 2H1" fill="none" stroke="#34465f"/></svg>
  <span style="left:504px;color:#e6e6e6;text-decoration:none">sign your lease online</span>
</div>

<!-- search band -->
<section class="abs search">
  <div class="big" style="left:59px;top:17px">YOU NEED TO STAY FROM</div>
  <div class="big" style="left:233px;top:17px">FROM</div>
  <div class="datebox" style="left:269px">
    <svg width="12" height="11" viewBox="0 0 12 11" aria-hidden="true"><rect x=".5" y="1.5" width="11" height="9" fill="none" stroke="#d8b11d"/><path d="M.5 4h11M3 0v3M9 0v3" stroke="#d8b11d"/></svg>02.12.2015</div>
  <div class="big" style="left:366px;top:17px">TO</div>
  <div class="datebox" style="left:386px">
    <svg width="12" height="11" viewBox="0 0 12 11" aria-hidden="true"><rect x=".5" y="1.5" width="11" height="9" fill="none" stroke="#d8b11d"/><path d="M.5 4h11M3 0v3M9 0v3" stroke="#d8b11d"/></svg>15.12.2015</div>
  <div class="label" style="left:506px;top:14px">HOUSEMATES:</div>
  <div class="label" style="left:592px;top:14px;background:var(--navy-dark);padding:0 3px">4</div>
  <div class="person on" style="left:506px"></div>
  <div class="person on" style="left:519px"></div>
  <div class="person on" style="left:533px"></div>
  <div class="person on" style="left:546px"></div>
  <div class="person" style="left:560px"></div>
  <div class="person" style="left:573px"></div>
  <div class="person" style="left:587px"></div>
  <div class="person" style="left:601px"></div>
  <div class="person" style="left:614px"></div>
  <div class="person" style="left:628px"></div>
  <div class="person" style="left:641px"></div>
  <div class="label" style="left:59px;top:48px">ROOM TYPE:</div>
  <div class="select">Single Room "Standard" <span style="float:right;margin-right:5px">⇕</span></div>
  <div class="label" style="left:246px;top:48px">WEEKLY RENT&nbsp; FROM</div>
  <div class="pricebox" style="left:362px;width:40px">$190 TO</div>
  <div class="pricebox" style="left:433px;width:41px">$690</div>
  <div class="btn-choose">FIND A ROOM</div>
</section>

<!-- rooms -->
<section class="abs rooms">
  <article class="card" style="left:59px">
    <div class="photo" role="img" aria-label="Photo of a bright double room with white sofas and a round glass table" style="background:linear-gradient(120deg,#dfe6ea,#a9b4bd 55%,#4a5766)"></div>
    <div class="kind">DOUBLE ROOM "STANDARD"</div>
    <div class="rate">$260 / WEEK</div>
    <div class="amen"><span><i></i>FIRE SAFETY</span><span><i></i>WI-FI</span><span><i></i>DESK</span></div>
    <div class="foot"><b>FREE NOW: 2</b><em>BOND 4 WEEKS – $1040</em></div>
    <span class="btn">SCHEDULE AN INSPECTION</span>
  </article>
  <article class="card" style="left:210px">
    <div class="photo" role="img" aria-label="Photo of a single room with a red armchair and large windows" style="background:linear-gradient(120deg,#e8e2dc,#c9b7ad 50%,#b5493a)"></div>
    <div class="kind">SINGLE ROOM "SUPERIOR"</div>
    <div class="rate">$280 / WEEK</div>
    <div class="amen"><span><i></i>FIRE SAFETY</span><span><i></i>WI-FI</span><span><i></i>DESK</span><span><i></i>ENSUITE</span><span style="width:90px"><i></i>WEEKLY CLEANING INCLUDED</span></div>
    <div class="foot"><b>FREE NOW: 3</b><em>BOND 4 WEEKS – $1120</em></div>
    <span class="btn">SCHEDULE AN INSPECTION</span>
  </article>
  <article class="card" style="left:360px">
    <div class="photo" role="img" aria-label="Photo of a double room with wooden wardrobe and a low bed" style="background:linear-gradient(120deg,#d3a06a,#b07a45 50%,#e8dccf)"></div>
    <div class="kind">DOUBLE ROOM "STANDARD"</div>
    <div class="rate">$260 / WEEK</div>
    <div class="amen"><span><i></i>FIRE SAFETY</span><span><i></i>WI-FI</span><span><i></i>ENSUITE</span></div>
    <div class="foot"><b>FREE NOW: 4</b><em>BOND 4 WEEKS – $1040</em></div>
    <span class="btn">SCHEDULE AN INSPECTION</span>
  </article>
  <article class="card" style="left:510px">
    <div class="photo" role="img" aria-label="Photo of a large master room with an attic window and a floral bedspread" style="background:linear-gradient(120deg,#f0ece4,#c9c2d8 55%,#6f4d8c)"></div>
    <div class="kind">MASTER SUITE "EXECUTIVE"</div>
    <div class="rate">$690 / WEEK</div>
    <div class="amen"><span><i></i>FIRE SAFETY</span><span><i></i>WI-FI</span><span><i></i>DESK</span><span><i></i>ENSUITE</span><span style="width:90px"><i></i>WEEKLY CLEANING INCLUDED</span></div>
    <div class="foot"><b>FREE NOW: 1</b><em>BOND 4 WEEKS – $2760</em></div>
    <span class="btn">SCHEDULE AN INSPECTION</span>
  </article>

  <div class="roundbtn" style="left:345px;top:207px"></div>
  <svg class="abs" style="left:351px;top:213px" width="13" height="13" viewBox="0 0 13 13" aria-hidden="true"><path d="M10.5 5A4.5 4.5 0 0 0 2.5 4M2.5 8a4.5 4.5 0 0 0 8 1" fill="none" stroke="#d8b11d" stroke-width="1.5"/><path d="M2 1v3h3M11 12V9H8" fill="none" stroke="#d8b11d" stroke-width="1.2"/></svg>
  <div class="abs more-label" style="left:337px;top:240px">SHOW MORE</div>
  <svg class="abs" style="left:305px;top:253px" width="9" height="9" viewBox="0 0 9 9" aria-hidden="true"><path d="M4 5 5 4M3 4 1.5 5.5a1.5 1.5 0 0 0 2 2L5 6M6 5l1.5-1.5a1.5 1.5 0 0 0-2-2L4 3" fill="none" stroke="#666" stroke-width=".8"/></svg>
  <div class="abs more-link" style="left:317px;top:253px">GO TO ROOMS CATALOG</div>
</section>

<!-- hot deals -->
<h2 class="abs sec-title" style="left:59px;top:666px">HOT DEALS!</h2>
<div class="abs hot">HOT!</div>
<div class="abs deal-slide" role="img" aria-label="Photo of a luxury bedroom with floral curtains, bedding and a vintage lamp"></div>
<div class="abs deal-box">
  <div class="a">PERFECT ROOM</div>
  <div class="b">LUXURY ROOM</div>
  <div class="c">FOR 2 PERSONS</div>
  <div class="d">JUST FOR $600 / MONTH</div>
</div>
<div class="slide-arrow" style="left:59px"></div>
<svg class="abs" style="left:64px;top:774px" width="10" height="12" viewBox="0 0 10 12" aria-hidden="true"><path d="M7 1 2 6l5 5" fill="none" stroke="#333"/></svg>
<div class="slide-arrow" style="left:334px"></div>
<svg class="abs" style="left:340px;top:774px" width="10" height="12" viewBox="0 0 10 12" aria-hidden="true"><path d="m3 1 5 5-5 5" fill="none" stroke="#333"/></svg>

<div class="tile" style="left:59px;width:96px;background:var(--teal);font-size:6.5px">
  <div class="inner"></div>
  <svg width="16" height="12" viewBox="0 0 16 12" aria-hidden="true" style="margin-bottom:4px"><circle cx="5.5" cy="6" r="4" fill="none" stroke="#fff" stroke-width="1.3"/><circle cx="10.5" cy="6" r="4" fill="none" stroke="#fff" stroke-width="1.3"/></svg>
  DOUBLE ROOMS<br>FOR COUPLES<br>30% DISCOUNT
</div>
<div class="tile" style="left:160px;width:95px;background:#2b2b2b;font-size:6px">
  <div class="inner"></div>
  WE GIVE YOU<br><span style="font-size:10px;line-height:11px">REWARDS</span>WHEN RENTING<br>2 ROOMS AT ONCE
  <svg width="10" height="8" viewBox="0 0 10 8" aria-hidden="true" style="margin-top:3px"><path d="M1 1h7v3a3 3 0 0 1-3 3H4a3 3 0 0 1-3-3z M8 2h1v2H8" fill="none" stroke="#fff"/></svg>
</div>
<div class="tile" style="left:259px;width:95px;background:var(--plum);font-size:6.5px;font-weight:500">
  <div class="inner"></div>
  <svg width="16" height="14" viewBox="0 0 16 14" aria-hidden="true" style="margin-bottom:4px"><path d="M2 2h8l4 5-4 5H2z" fill="none" stroke="#fff" stroke-width="1.2"/><text x="4" y="9.5" font-size="6" fill="#fff" font-family="Arial">%</text></svg>
  TIME TO BOOK:<br><span style="font-size:8.5px;line-height:9.5px">LUXURY FOR THE<br>SUPERIOR PRICE</span>
</div>
<div class="pager" style="left:166px"></div>
<div class="pager" style="left:189px;background:#222"></div>
<div class="pager" style="left:211px"></div>
<div class="pager" style="left:234px"></div>

<!-- reviews -->
<h2 class="abs sec-title" style="left:410px;top:666px">REVIEWS ABOUT OUR ROOMS</h2>
<div class="abs promo">
  <svg class="abs" style="left:12px;top:8px" width="22" height="18" viewBox="0 0 22 18" aria-hidden="true"><path d="M2 2h14l4 7-4 7H2z" fill="none" stroke="#1f2633" stroke-width="1.5"/><text x="6" y="12.5" font-size="8" font-weight="700" fill="#1f2633" font-family="Arial">%</text></svg>
  <div class="cut"></div>
  <span>WRITE REVIEW – GET A DISCOUNT ON<br>YOUR NEXT RENT</span>
</div>

<article class="review" style="top:742px">
  <div class="avatar"><div role="img" aria-label="Tenant portrait photo" style="background:linear-gradient(160deg,#6a5b52,#2f2a28)"></div></div>
  <div class="who"><b>MIRA OSTVALD</b><small>TENANT FROM 14.08.2015<br>TO 15.11.2015</small></div>
  <div class="rating"><span class="lbl">MY RATING:</span>
    <svg width="50" height="10" viewBox="0 0 50 10" aria-hidden="true"><g fill="#3aa53a"><path id="st" d="M5 0l1.5 3.2 3.5.4-2.6 2.4.7 3.5L5 7.8 1.9 9.5l.7-3.5L0 3.6l3.5-.4z"/><use href="#st" x="10"/><use href="#st" x="20"/><use href="#st" x="30"/></g><use href="#st" x="40" fill="#d0d0d0"/></svg>
    <span class="score">4/5</span></div>
  <p>I moved into this house last month. Wonderful place!<br>And what a view from my window ... hmmm ...! The housemates are quiet and friendly, and every problem is fixed within a day. The inspection was easy to book and the contract was signed online. Thanks to the house manager!</p>
</article>

<article class="review" style="top:842px">
  <div class="avatar"><div role="img" aria-label="Tenant portrait photo" style="background:linear-gradient(160deg,#e6c7ae,#b98a6c)"></div></div>
  <div class="who"><b>JON DERROW</b><small>TENANT FROM 14.08.2015<br>TO 15.11.2015</small></div>
  <div class="rating"><span class="lbl">MY RATING:</span>
    <svg width="50" height="10" viewBox="0 0 50 10" aria-hidden="true"><g fill="#3aa53a"><use href="#st"/><use href="#st" x="10"/><use href="#st" x="20"/><use href="#st" x="30"/><use href="#st" x="40"/></g></svg>
    <span class="score">5/5</span></div>
  <p>Large beautiful rooms. The windows offer views of the Velmara River and the hills. The house is clean, safe and well looked after, with smoke alarms in every room. The only negative is perhaps the cold water in the morning, but ...<br><a>»»» SHOW FULL REVIEW</a></p>
</article>

<article class="review" style="top:944px">
  <div class="avatar" style="border-color:#f2a900"><div role="img" aria-label="Tenant portrait photo" style="background:linear-gradient(160deg,#4b3a30,#1f1a18)"></div></div>
  <div class="who"><b>ASHER PRYCE</b><small>TENANT FROM 14.08.2015<br>TO 15.11.2015</small></div>
  <div class="rating"><span class="lbl">MY RATING:</span>
    <svg width="50" height="10" viewBox="0 0 50 10" aria-hidden="true"><g fill="#f2a900"><use href="#st"/><use href="#st" x="10"/><use href="#st" x="20"/></g><g fill="#d0d0d0"><use href="#st" x="30"/><use href="#st" x="40"/></g></svg>
    <span class="score">3/5</span></div>
  <p>The big negative was the shared kitchen: it was often busy in the evening and the fridge space was small. But despite these shortcomings, the room is great and I want to thank house manager Marena!</p>
</article>

<div class="abs" style="left:410px;top:1042px;width:243px;height:3px;background:#e3e3e3"></div>
<div class="roundbtn" style="left:519px;top:1050px;width:18px;height:18px"></div>
<svg class="abs" style="left:523px;top:1054px" width="10" height="10" viewBox="0 0 13 13" aria-hidden="true"><path d="M10.5 5A4.5 4.5 0 0 0 2.5 4M2.5 8a4.5 4.5 0 0 0 8 1" fill="none" stroke="#d8b11d" stroke-width="1.6"/></svg>
<div class="abs more-label" style="left:505px;top:1071px;font-size:4.5px">OTHER REVIEWS</div>
<svg class="abs" style="left:487px;top:1079px" width="8" height="8" viewBox="0 0 9 9" aria-hidden="true"><path d="M4 5 5 4M3 4 1.5 5.5a1.5 1.5 0 0 0 2 2L5 6M6 5l1.5-1.5a1.5 1.5 0 0 0-2-2L4 3" fill="none" stroke="#666" stroke-width=".8"/></svg>
<div class="abs more-link" style="left:498px;top:1079px;font-size:4.5px">READ MORE REVIEWS</div>

<!-- footer -->
<footer class="abs footer">
  <div class="col" style="left:61px;top:10px"><span class="light">Messages</span><span class="strong">ROOMS</span></div>
  <div class="col" style="left:114px;top:10px"><span class="light">List your room</span><span class="strong">OUR HOUSES</span></div>
  <div class="col" style="left:168px;top:10px"><span class="light">reviews</span><span class="strong" style="margin-left:13px">CONTACTS</span></div>
  <div class="feedback">Feedback</div>
  <svg class="abs" style="left:265px;top:19px" width="8" height="7" viewBox="0 0 8 7" aria-hidden="true"><rect x=".5" y=".5" width="7" height="5" fill="none" stroke="#d8b11d"/></svg>
  <svg class="abs" style="left:362px;top:16px" width="8" height="10" viewBox="0 0 8 10" aria-hidden="true"><path d="M4 1a3 3 0 0 0-3 3c0 2 3 5 3 5s3-3 3-5a3 3 0 0 0-3-3z" fill="none" stroke="#d8b11d"/></svg>
  <span class="info" style="left:374px;text-decoration:none">Velmora, Orlinaya str, 1A</span>
  <svg class="abs" style="left:477px;top:15px" width="10" height="12" viewBox="0 0 10 12" aria-hidden="true"><rect x="2.5" y=".5" width="5" height="11" rx="1" fill="none" stroke="#d8b11d"/></svg>
  <span class="info" style="left:493px">+7 (800) 555-01-42</span>
  <svg class="abs" style="left:566px;top:17px" width="10" height="8" viewBox="0 0 10 8" aria-hidden="true"><rect x=".5" y=".5" width="9" height="7" fill="none" stroke="#d8b11d"/><path d="m.5.5 4.5 4 4.5-4" fill="none" stroke="#d8b11d"/></svg>
  <span class="info" style="left:581px;text-decoration:none">stay@lodvenra.com</span>
</footer>
<div class="abs copy"><span>© 2015 Lodvenra House-share</span></div>

</body>
</html>
```